Brindle Works Business Card

We need a business card design for an existing company (www.brindle-works.example). The business cards will be by Pavo in their Velta range (http://uk.pavoprint.example/products/velta/business-cards.html).

The card should be landscape, with the full company logo on the reverse side. I would like to have the card to portray a professional image (this is a high technology niche consultancy company). The card should be mostly white but aligned with our website (this is mostly dark colours). I can supply the logo files etc.

Details on the card should include the following:

Name (example: Martin Oakbury)
Position (example: Principal Consultant)
Email Address (example: martin@brindle-works.example)
Mobile Phone Number (example: +44 (0) 7912 604 385)
Website (example: www.brindle-works.example)
Twitter (example: @brindleworksco)
Facebook (example: www.facebook.com/brindleworksco)

I would like the text on the front of the card to be black. Thanks.

Industry/Entity Type

Business

Requirements
Should not have
• The company address on the card.

```html
<!DOCTYPE html>
<html lang="en">
<head>
<meta charset="utf-8">
<title>Brindle Works Business Card</title>
<link rel="stylesheet" href="https://fonts.googleapis.com/css2?family=Carlito:wght@400;700&family=Open+Sans:wght@400;600;700&display=swap">
<style>
  :root {
    --stage: #d9d4cb;
    --card-light: #e4e5e7;
    --card-dark: #1f1f20;
    --band-grey: #454648;
    --pill-grey: #58595b;
    --orange: #f26c1c;
    --orange-soft: #f7913f;
    --text-grey: #55565a;
    --white: #ffffff;
    --black: #111111;
  }
  * { box-sizing: border-box; margin: 0; padding: 0; }
  html, body { width: 1200px; height: 916px; overflow: hidden; }
  body { background: var(--stage); position: relative; font-family: "Open Sans", Arial, sans-serif; }

  .card {
    position: absolute;
    width: 560px;
    height: 320px;
    overflow: hidden;
    box-shadow: 0 8px 22px rgba(0,0,0,.28);
  }
  .band { position: absolute; left: 0; right: 0; height: 12px; background: var(--band-grey); }
  .band--top { top: 0; }
  .band--bottom { bottom: 0; }
  .band__accent { position: absolute; top: 0; bottom: 0; background: var(--orange); }

  /* Front */
  .card--front { left: 60px; top: 150px; background: var(--card-light); }
  .card--front .band--top .band__accent { left: 33%; width: 29%; }
  .card--front .band--bottom .band__accent { left: 68%; width: 20%; }
  .brand { position: absolute; left: 36px; top: 124px; display: flex; align-items: center; gap: 16px; }
  .brand__dot { width: 66px; height: 66px; border-radius: 50%; background: var(--orange); flex: none; }
  .brand__name {
    font-family: "Open Sans", Arial, sans-serif; font-weight: 700; font-size: 24px;
    letter-spacing: .8px; color: var(--orange); text-transform: uppercase; line-height: 1;
    white-space: nowrap;
  }
  .brand__tagline { margin-top: 8px; font-size: 16px; color: var(--text-grey); letter-spacing: .5px; white-space: nowrap; }

  /* Back */
  .card--back { left: 590px; top: 440px; background: var(--card-dark); font-family: "Carlito", Calibri, sans-serif; }
  .card--back .band--top .band__accent { left: 34%; width: 32%; }
  .contacts { position: absolute; left: 70px; top: 50px; font-size: 16px; line-height: 21px; border-collapse: collapse; }
  .contacts th { color: var(--white); font-weight: 400; text-align: left; padding-right: 6px; }
  .contacts .sep { color: var(--white); padding-right: 8px; }
  .contacts td.value { color: var(--orange); font-weight: 700; }

  .role-mark { position: absolute; right: 94px; bottom: 64px; width: 86px; height: 86px; border-radius: 50%; background: var(--orange-soft); opacity: .45; }
  .role-tab {
    position: absolute; right: 0; bottom: 96px; height: 34px; width: 248px;
    background: var(--orange); border-radius: 17px 0 0 17px;
    display: flex; align-items: center; padding-left: 26px;
    font-weight: 700; font-size: 17px; color: var(--black);
  }
  .name-pill {
    position: absolute; left: 104px; bottom: 50px; width: 270px; height: 38px;
    background: var(--pill-grey); border-radius: 19px;
    display: flex; align-items: center; padding-left: 18px;
    color: #e8e8e8; font-size: 21px; letter-spacing: 2px; text-transform: uppercase;
    white-space: nowrap;
    box-shadow: 0 2px 4px rgba(0,0,0,.5);
  }
</style>
</head>
<body>
  <section class="card card--front" aria-label="Card front">
    <div class="band band--top"><span class="band__accent"></span></div>
    <div class="brand">
      <span class="brand__dot"></span>
      <div>
        <p class="brand__name">Brindle Works Solutions</p>
        <p class="brand__tagline">Your Systems - Your Network - Our Craft</p>
      </div>
    </div>
    <div class="band band--bottom"><span class="band__accent"></span></div>
  </section>

  <section class="card card--back" aria-label="Card back">
    <div class="band band--top"><span class="band__accent"></span></div>
    <table class="contacts">
      <tr><th>Email</th><td class="sep">:</td><td class="value">martin@brindle-works.example</td></tr>
      <tr><th>Mobile</th><td class="sep">:</td><td class="value">+44 (0) 7912 604 385</td></tr>
      <tr><th>Website</th><td class="sep">:</td><td class="value">www.brindle-works.example</td></tr>
      <tr><th>Twitter</th><td class="sep">:</td><td class="value">@brindleworksco</td></tr>
      <tr><th>Facebook</th><td class="sep">:</td><td class="value">www.facebook.com/brindleworksco</td></tr>
    </table>
    <span class="role-mark"></span>
    <div class="role-tab">Principal Consultant</div>
    <div class="name-pill">Martin Oakbury</div>
  </section>
</body>
</html>
```